Short term vacation rental

I need a simple site the we can rent a duplex that is on the sand in Indian rocks beach Fl needs to be able to sync with multiple calendars like staylumo.com qelt tovn using Wordpress

```html
<!DOCTYPE html>
<html lang="en">
<head>
<meta charset="utf-8">
<title>Tidewell Retreats — Indian Rocks Beach Duplex</title>
<link href="https://fonts.googleapis.com/css2?family=Inter:wght@400;500;600;700&family=Playfair+Display:ital,wght@0,400;0,600;0,700;1,700;1,800&display=swap" rel="stylesheet">
<style>
  :root {
    --ink: #1d2326;
    --muted: #4d5558;
    --accent: #1a6f97;
    --accent-dark: #0f5f8c;
    --paper: #f8f8f8;
    --paper-cool: #f3f3f5;
    --dark: #2f3030;
    --dark-text: #c9cccc;
    --icon-blue: #7fb8e8;
    --card: #ffffff;
    --halo: #e4f2f6;
    --line: #dcdfe1;
    --hero-a: #2a7c88;
    --hero-b: #1d6f7b;
    --photo-day-a: #4a8aa0;
    --photo-day-b: #3a7b8e;
    --photo-dusk-a: #7d6d72;
    --photo-dusk-b: #6d5c5e;
  }
  * { box-sizing: border-box; margin: 0; padding: 0; }
  html, body { width: 1200px; height: 2858px; overflow: hidden; }
  body { position: relative; background: var(--paper); font-family: "Inter", sans-serif; color: var(--ink); }

  /* Hero */
  .hero { position: absolute; left: 0; top: 0; width: 1200px; height: 574px; overflow: hidden; }
  .hero-photo { position: absolute; inset: 0; background: linear-gradient(180deg, var(--hero-a) 0%, var(--hero-b) 100%); }
  .nav { position: absolute; left: 0; top: 0; width: 1200px; height: 32px; background: #c2a3a3; border-bottom: 1px solid rgba(255,255,255,.25); }
  .nav-brand { position: absolute; left: 199px; top: 10px; font-family: "Playfair Display", serif; font-size: 9px; letter-spacing: 1.5px; color: #4b5b66; }
  .nav-links { position: absolute; left: 471px; top: 9px; display: flex; gap: 16px; font-size: 9.5px; font-weight: 500; color: #3d4a52; }
  .nav-links .active { color: var(--accent); border-bottom: 1.5px solid var(--accent); padding-bottom: 3px; }
  .nav-cta { position: absolute; left: 924px; top: 7px; width: 76px; height: 17px; border-radius: 9px; background: var(--accent-dark); color: #fff; font-size: 9px; font-weight: 600; text-align: center; line-height: 17px; }
  .hero-title { position: absolute; left: 200px; top: 298px; font-family: "Playfair Display", serif; font-style: italic; font-weight: 800; font-size: 30px; line-height: 30px; color: #fff; letter-spacing: -0.5px; }
  .hero-sub { position: absolute; left: 200px; top: 371px; width: 270px; padding-left: 16px; border-left: 1.5px solid rgba(255,255,255,.6); font-size: 11px; line-height: 18px; color: #fff; }
  .hero-vertical { position: absolute; left: 989px; top: 150px; writing-mode: vertical-rl; font-size: 8px; letter-spacing: 1.6px; color: rgba(255,255,255,.75); }
  .hero-chevron { position: absolute; left: 594px; top: 524px; }

  /* Wings */
  .wing-halo { position: absolute; background: var(--halo); border-radius: 6px; }
  .wing-photo { position: absolute; border-radius: 8px; box-shadow: 0 10px 24px rgba(30,60,80,.18); }
  .photo-solis { left: 150px; top: 614px; width: 430px; height: 537px; background: linear-gradient(180deg, var(--photo-day-a), var(--photo-day-b)); }
  .photo-luna { left: 620px; top: 1231px; width: 430px; height: 538px; background: linear-gradient(180deg, var(--photo-dusk-a), var(--photo-dusk-b)); }
  .wing-label { position: absolute; font-size: 9px; font-weight: 600; letter-spacing: 2px; color: var(--accent); }
  .wing-heading { position: absolute; font-family: "Playfair Display", serif; font-weight: 600; font-size: 25px; line-height: 27px; color: var(--ink); }
  .wing-text { position: absolute; font-size: 10px; line-height: 16.5px; color: var(--muted); }
  .wing-link { position: absolute; font-size: 9px; font-weight: 600; color: var(--accent); border-bottom: 1px solid var(--accent); padding-bottom: 2px; }
  .align-right { text-align: right; }

  /* Textures */
  .textures { position: absolute; left: 0; top: 1808px; width: 1200px; height: 575px; background: var(--dark); }
  .textures-title { position: absolute; left: 200px; top: 178px; font-family: "Playfair Display", serif; font-weight: 600; font-size: 30px; line-height: 35px; color: #fff; }
  .texture { position: absolute; top: 290px; width: 250px; }
  .texture-title { margin-top: 10px; font-family: "Playfair Display", serif; font-style: italic; font-weight: 700; font-size: 15px; color: #fff; }
  .texture-text { margin-top: 10px; font-size: 10px; line-height: 16px; color: var(--dark-text); }

  /* Experience */
  .experience { position: absolute; left: 0; top: 2383px; width: 1200px; height: 330px; background: var(--paper-cool); }
  .exp-label { position: absolute; left: 150px; top: 44px; font-size: 9px; font-weight: 600; letter-spacing: 2px; color: var(--accent); }
  .exp-title { position: absolute; left: 150px; top: 65px; font-family: "Playfair Display", serif; font-weight: 600; font-size: 24px; color: var(--ink); }
  .exp-intro { position: absolute; left: 810px; top: 66px; width: 240px; font-size: 10px; line-height: 16px; color: var(--muted); }
  .moment { position: absolute; width: 213px; height: 117px; background: var(--card); border-radius: 6px; padding: 22px 20px; box-shadow: 0 2px 10px rgba(0,0,0,.04); }
  .moment-time { font-size: 8.5px; color: #6e9fb8; letter-spacing: .5px; }
  .moment-title { margin-top: 10px; font-family: "Playfair Display", serif; font-size: 15px; color: var(--ink); }
  .moment-text { margin-top: 8px; font-size: 10px; line-height: 16px; color: var(--muted); }

  /* Footer */
  .footer { position: absolute; left: 0; top: 2712px; width: 1200px; height: 146px; background: var(--paper-cool); border-top: 1px solid var(--line); }
  .footer-brand { position: absolute; left: 200px; top: 40px; font-family: "Playfair Display", serif; font-size: 14px; letter-spacing: 1.5px; color: #2c4f66; }
  .footer-tag { position: absolute; left: 200px; top: 80px; font-size: 10px; line-height: 16px; color: var(--muted); }
  .footer-links { position: absolute; left: 471px; top: 73px; display: flex; gap: 15px; font-size: 10px; color: var(--muted); }
  .footer-copy { position: absolute; right: 200px; top: 66px; text-align: right; font-size: 7.5px; line-height: 10px; color: #8a9194; }
  .reserve { position: absolute; left: 1008px; top: 90px; width: 172px; height: 33px; border-radius: 17px; background: var(--accent-dark); color: #fff; font-size: 8.5px; font-weight: 700; letter-spacing: .8px; padding-left: 15px; line-height: 33px; white-space: nowrap; box-shadow: 0 4px 12px rgba(15,95,140,.3); }
  .reserve-icon { position: absolute; right: 4px; top: 4px; width: 25px; height: 25px; border-radius: 50%; background: #fff; }
</style>
</head>
<body>

<header class="hero">
  <div class="hero-photo" role="img" aria-label="Photograph of a calm turquoise Gulf sea under a pink dusk sky"></div>
  <nav class="nav">
    <div class="nav-brand">TIDEWELL RETREATS</div>
    <div class="nav-links">
      <span class="active">The Duplex</span><span>Amenities</span><span>Availability</span><span>Gallery</span><span>Location</span>
    </div>
    <div class="nav-cta">Book Now</div>
  </nav>
  <h1 class="hero-title">The Rhythms<br>of the Shore</h1>
  <p class="hero-sub">A luxury duplex designed to synchronize your soul with the ebb and flow of Indian Rocks Beach.</p>
  <div class="hero-vertical">ESTABLISHED 2024 — INDIAN ROCKS BEACH, FL</div>
  <svg class="hero-chevron" width="12" height="14" viewBox="0 0 12 14" fill="none" stroke="#fff" stroke-width="1.6"><path d="M1 1l5 5 5-5M1 7l5 5 5-5"/></svg>
</header>

<section class="wing wing-east">
  <div class="wing-halo" style="left:130px;top:602px;width:468px;height:565px;transform:rotate(-1.2deg);"></div>
  <div class="wing-photo photo-solis" role="img" aria-label="Photograph of a modern white three-storey villa with glass walls, palm trees and an infinity pool"></div>
  <div class="wing-label" style="left:620px;top:798px;">EAST WING: SOLIS</div>
  <h2 class="wing-heading" style="left:620px;top:826px;">Awaken with the<br>morning light.</h2>
  <p class="wing-text" style="left:620px;top:896px;width:430px;">Unit A is an ode to the sunrise. With sprawling eastern terraces and an open-concept living area, every morning becomes a curated event of gold and amber hues. Designed for the early risers and the coffee-sippers.</p>
  <span class="wing-link" style="left:620px;top:957px;">Explore Solis Interior</span>
</section>

<section class="wing wing-west">
  <div class="wing-halo" style="left:602px;top:1217px;width:466px;height:560px;transform:rotate(1.4deg);"></div>
  <div class="wing-photo photo-luna" role="img" aria-label="Photograph of a wooden sun deck with loungers over the water at sunset"></div>
  <div class="wing-label" style="left:150px;top:1416px;width:430px;text-align:right;">WEST WING: LUNA</div>
  <h2 class="wing-heading align-right" style="left:150px;top:1443px;width:430px;">Retreat into the<br>velvet evening.</h2>
  <p class="wing-text align-right" style="left:150px;top:1512px;width:430px;">Unit B celebrates the twilight. Oriented toward the Gulf sunsets, the rooftop deck offers an unobstructed view of the sun dipping below the horizon. A sanctuary for cocktails, conversation, and the cooling salt breeze.</p>
  <span class="wing-link" style="left:483px;top:1574px;">Explore Luna Interior</span>
</section>

<section class="textures">
  <h2 class="textures-title">The Textures<br>of Tranquility</h2>
  <div class="texture" style="left:200px;">
    <svg width="22" height="18" viewBox="0 0 22 18" fill="none" stroke="var(--icon-blue)" stroke-width="1.6"><path d="M1 3c3-2 5 2 8 0s5 2 8 0 4 0 4 0M1 9c3-2 5 2 8 0s5 2 8 0 4 0 4 0M1 15c3-2 5 2 8 0s5 2 8 0 4 0 4 0"/></svg>
    <div class="texture-title">The Sound</div>
    <p class="texture-text">The rhythmic pulse of the Gulf waves provides a natural white noise that guarantees the deepest sleep of your life.</p>
  </div>
  <div class="texture" style="left:477px;">
    <svg width="22" height="18" viewBox="0 0 22 22" fill="none" stroke="var(--icon-blue)" stroke-width="1.6"><circle cx="11" cy="11" r="4.5"/><path d="M11 1v3M11 18v3M1 11h3M18 11h3M4 4l2 2M16 16l2 2M4 18l2-2M16 6l2-2"/></svg>
    <div class="texture-title">The Warmth</div>
    <p class="texture-text">Heated sand paths and sun-drenched private decks capture the Floridian heat, keeping the chill at bay long after sunset.</p>
  </div>
  <div class="texture" style="left:753px;">
    <svg width="22" height="18" viewBox="0 0 22 18" fill="none" stroke="var(--icon-blue)" stroke-width="1.6"><path d="M1 6h13a3 3 0 1 0-3-3M1 11h17a3 3 0 1 1-3 3M1 16h8"/></svg>
    <div class="texture-title">The Scent</div>
    <p class="texture-text">The crisp, iodine tang of the salt air mixed with blooming jasmine from our private tropical gardens.</p>
  </div>
</section>

<section class="experience">
  <div class="exp-label">THE EXPERIENCE</div>
  <h2 class="exp-title">Circadian Living</h2>
  <p class="exp-intro">A choreographed flow of moments, from the first light to the final star.</p>
  <article class="moment" style="left:150px;top:132px;">
    <div class="moment-time">06:45 AM</div><div class="moment-title">Ocean Dawn</div>
    <p class="moment-text">French press on the deck as the world turns gold.</p>
  </article>
  <article class="moment" style="left:379px;top:172px;">
    <div class="moment-time">12:30 PM</div><div class="moment-title">Gulf Drift</div>
    <p class="moment-text">Paddleboarding the glass-flat waters of the morning tide.</p>
  </article>
  <article class="moment" style="left:608px;top:112px;">
    <div class="moment-time">06:15 PM</div><div class="moment-title">Salt &amp; Citrus</div>
    <p class="moment-text">Rooftop aperitifs as the sky ignites in violet.</p>
  </article>
  <article class="moment" style="left:837px;top:152px;">
    <div class="moment-time">10:00 PM</div><div class="moment-title">Moonlit Tide</div>
    <p class="moment-text">A warm plunge in the courtyard pool under the stars.</p>
  </article>
</section>

<footer class="footer">
  <div class="footer-brand">TIDEWELL RETREATS</div>
  <p class="footer-tag">Redefining luxury rental through<br>intentional design and coastal harmony.</p>
  <div class="footer-links"><span>Privacy Policy</span><span>Terms of Service</span><span>Contact Us</span><span>Guest Guide</span></div>
  <div class="footer-copy">© 2024 Shorehaus Indian Rocks Beach.<br>All rights reserved.</div>
  <div class="reserve">RESERVE YOUR ESCAPE
    <span class="reserve-icon"><svg width="25" height="25" viewBox="0 0 25 25" fill="none" stroke="var(--accent-dark)" stroke-width="1.6"><path d="M8.5 16.5l8-8M10 8.5h6.5V15"/></svg></span>
  </div>
</footer>

</body>
</html>
```